Redesign Login page

I want to redesign my login page to bring my 2 products closer together. I am only looking to redesign one login page, not 2.

For the logo, please make it solid and it can be black or white if helpful. I can also fine tune the logo if you get it close.

Coded - Design and coding required

1 page

```html
<!DOCTYPE html>
<html lang="en">
<head>
<meta charset="utf-8">
<title>Velora – Log in</title>
<link rel="stylesheet" href="https://fonts.googleapis.com/css2?family=Inter:wght@400;500;600;700&family=Lato:wght@400;700;900&display=swap">
<style>
  :root {
    --teal: #12ab93;
    --ink: #111111;
    --muted: #555b61;
    --field-border: #d4d6d9;
    --social-bg: #f2f3f5;
    --white: #ffffff;
    --panel-top: #2a2624;
    --panel-mid: #1c1a19;
    --panel-bottom: #0e0e0f;
  }
  * { box-sizing: border-box; margin: 0; padding: 0; }
  html, body { width: 1200px; height: 782px; overflow: hidden; background: var(--white); }
  body { font-family: "Inter", sans-serif; color: var(--ink); position: relative; }

  .hero {
    position: absolute; left: 0; top: 0; width: 400px; height: 782px;
    background: linear-gradient(180deg, var(--panel-top) 0%, var(--panel-mid) 55%, var(--panel-bottom) 100%);
    color: var(--white);
  }
  .hero__brand {
    position: absolute; left: 48px; top: 44px;
    font-family: "Lato", sans-serif; font-weight: 900; font-size: 40px; letter-spacing: -1px;
    display: flex; align-items: center; gap: 10px;
  }
  .hero__brand-dot { width: 18px; height: 18px; border-radius: 50%; background: var(--white); }
  .hero__quote {
    position: absolute; left: 42px; top: 573px; width: 330px;
    font-family: "Lato", sans-serif; font-size: 26px; line-height: 38px;
  }
  .hero__name { position: absolute; left: 42px; top: 680px; font-family: "Lato", sans-serif; font-size: 20px; }
  .hero__role { position: absolute; left: 42px; top: 711px; font-size: 14px; color: #e8e8e8; }

  .login { position: absolute; left: 652px; top: 0; width: 300px; }
  .login__title {
    position: absolute; left: -150px; width: 600px; top: 60px; text-align: center;
    font-family: "Lato", sans-serif; font-weight: 700; font-size: 32px; letter-spacing: -0.4px;
  }
  .login__lead {
    position: absolute; left: -150px; width: 600px; top: 105px; text-align: center;
    font-size: 15.5px; line-height: 24px; color: var(--muted);
  }
  .field {
    position: absolute; left: 0; width: 300px; border: 1px solid var(--field-border); border-radius: 2px;
    padding: 7px 7px;
  }
  .field--email { top: 183px; height: 47px; }
  .field--password { top: 246px; height: 49px; border: 2px solid var(--teal); border-radius: 3px; padding: 7px 6px; }
  .field__label { font-size: 12px; color: var(--muted); display: block; }
  .field__value { font-size: 12.5px; margin-top: 4px; display: block; }
  .field__caret { display: inline-block; width: 1px; height: 14px; background: var(--ink); vertical-align: -2px; }

  .link { color: var(--teal); font-weight: 600; text-decoration: none; }
  .login__forgot { position: absolute; top: 311px; left: 0; font-size: 13.5px; letter-spacing: 0.3px; }

  .remember { position: absolute; top: 342px; left: 0; width: 300px; display: flex; justify-content: space-between; align-items: center; }
  .remember__label { font-size: 12px; color: var(--muted); letter-spacing: 0.2px; }
  .toggle { width: 48px; height: 24px; border-radius: 12px; background: var(--teal); position: relative; }
  .toggle::after { content: ""; position: absolute; right: 3px; top: 3px; width: 18px; height: 18px; border-radius: 50%; background: var(--white); }

  .btn-primary {
    position: absolute; top: 396px; left: 0; width: 300px; height: 46px; border-radius: 23px;
    background: var(--teal); color: var(--white); font-weight: 600; font-size: 15px; letter-spacing: 0.6px;
    display: flex; align-items: center; justify-content: center;
  }
  .divider { position: absolute; top: 478px; left: 7px; width: 286px; display: flex; align-items: center; gap: 8px; font-size: 12px; color: var(--muted); }
  .divider::before, .divider::after { content: ""; flex: 1; height: 1px; background: var(--field-border); }

  .social {
    position: absolute; left: 0; width: 300px; height: 44px; border-radius: 22px; background: var(--social-bg);
    display: flex; align-items: center; justify-content: center; font-weight: 700; font-size: 14.5px; letter-spacing: 0.6px;
  }
  .social__mark { position: absolute; left: 10px; top: 7px; width: 30px; height: 30px; border-radius: 50%; }
  .social--search { top: 521px; } .social--search .social__mark { background: #4b83e8; }
  .social--friend { top: 576px; } .social--friend .social__mark { background: #1a8ef0; }
  .social--orchard { top: 631px; } .social--orchard .social__mark { background: #111; width: 22px; height: 22px; left: 14px; top: 11px; }

  .signup { position: absolute; top: 705px; left: -50px; width: 400px; text-align: center; font-size: 12.5px; color: var(--muted); }
  .signup .link { font-size: 14.5px; margin-left: 4px; }
</style>
</head>
<body>
  <aside class="hero" role="img" aria-label="Photograph of a project manager in glasses holding a tablet beside a window">
    <div class="hero__brand"><span>Velora</span><span class="hero__brand-dot"></span></div>
    <p class="hero__quote">"All the resources my team and I require, simply put."</p>
    <p class="hero__name">Jane Doe</p>
    <p class="hero__role">Project Manager @ Northfield School</p>
  </aside>

  <main class="login">
    <h1 class="login__title">Welcome back to Velora</h1>
    <p class="login__lead">Manage all your documents in one place with<br>our powerful management system</p>

    <div class="field field--email">
      <span class="field__label">Email</span>
      <span class="field__value">janedoe@mailbox.com</span>
    </div>
    <div class="field field--password">
      <span class="field__label">Password</span>
      <span class="field__value">**************<span class="field__caret"></span></span>
    </div>

    <a class="link login__forgot" href="#">Forgot password?</a>

    <div class="remember">
      <span class="remember__label">Remember sign in details</span>
      <span class="toggle"></span>
    </div>

    <div class="btn-primary">Log In</div>

    <div class="divider">OR</div>

    <div class="social social--search"><span class="social__mark"></span>Continue with Searchly</div>
    <div class="social social--friend"><span class="social__mark"></span>Continue with Friendbook</div>
    <div class="social social--orchard"><span class="social__mark"></span>Continue with Orchard</div>

    <p class="signup">Don't have an account? <a class="link" href="#">Sign up</a></p>
  </main>
</body>
</html>
```